Logo and Flyer for Co-Branded Comedy Show

Graphic designer needed to create a promotional flyer for a comedy show. Two different comedy shows, with distinct branding, are joining forces to create a combined show. (co-branded logo to be included is attached.)

The design of the promotional materials should be a modern take on a vintage poster a la Quirkwood Jamboree. We'd like it to be a vintage look with a modern twist (I have attached the Quirkwood Jamboree Flyer for reference - marked up with info for our show) Filename: PLGRVN Flyer Mark Up

Images of the two hosts are attached: Filenames:

Our show will be in a theater, so if it can play off a playbill that would be great. I have attached examples of the clean look that we like, as well as some vintage theater flyers. We'd like to stay on the lighter side of the color palette (light gray, blues, etc. which is in line with the Harbor Laughs Live flyer) Filename: PLGR VN Flyer Direction

Current Branding of the individual Shows
I have attached the current promo materials for the individual shows, so you have a sense of the color palette and logo treatment.

The deliverable:
1 flyer vertical, 1 flyer horizontal - same design/concept but in 2 orientation (vertical and horizontal) horizontal will be used for web.
***This flyer will include the co-branded logo seen attached - Harbor Laughs Live Gets Real Honest (individual logos already created and attached) - Download PSD File here: http://lnk.example-short.test/PLGRVN

Industry/Entity Type

Graphic Designer

Colors
0493cd
85cae6
ecf7fb
f5f5f5
ffffff
606060
fbfbfb
0255a3
3176b5

Requirements
Must have
• Vintage look with a modern twist
• Vertical and horizontal options

```html
<!DOCTYPE html>
<html lang="en">
<head>
<meta charset="utf-8">
<title>Harbor Laughs Live Gets Real Honest</title>
<link rel="stylesheet" href="https://fonts.googleapis.com/css2?family=Alfa+Slab+One&family=Oswald:wght@200;300;400;500;600&display=swap">
<style>
  :root {
    --sky: #6bc9e6;
    --ink: #111111;
    --paper: #ffffff;
    --photo-light: #e6e6e6;
    --photo-dark: #5a5a5a;
  }
  html, body { margin: 0; padding: 0; overflow: hidden; }
  body { width: 1200px; height: 2236px; background: var(--sky); }
  .poster { display: block; width: 1200px; height: 2236px; }

  .slab { font-family: "Alfa Slab One", serif; }
  .condensed { font-family: "Oswald", sans-serif; }

  .ink { fill: var(--ink); }
  .paper { fill: var(--paper); }
  .sky { fill: var(--sky); }

  .presenter-name { font-weight: 600; font-size: 52px; }
  .presenter-sub { font-weight: 500; font-size: 17px; letter-spacing: 3px; }
  .rule-label { font-weight: 400; font-size: 38px; }
  .title-main { font-size: 172px; }
  .title-sub { font-size: 106px; }
  .host-name { font-size: 28px; }
  .ampersand { font-size: 150px; }
  .lineup { font-weight: 300; font-size: 74px; }
  .one-night { font-size: 46px; }
  .show-date { font-weight: 200; font-size: 150px; }
  .venue { font-weight: 400; font-size: 38px; }
  .badge-text { font-weight: 500; font-size: 17px; }
  .site { font-weight: 500; font-size: 54px; }
</style>
</head>
<body>
<svg class="poster" width="1200" height="2236" viewBox="0 0 1200 2236" xmlns="http://www.w3.org/2000/svg">
  <defs>
    <radialGradient id="photoTone" cx="50%" cy="42%" r="62%">
      <stop offset="0" stop-color="#e6e6e6"/>
      <stop offset="1" stop-color="#5a5a5a"/>
    </radialGradient>
  </defs>

  <!-- presenter -->
  <text class="condensed presenter-name ink" x="601" y="100" text-anchor="middle" textLength="262" lengthAdjust="spacingAndGlyphs">PALEWOOD</text>
  <text class="condensed presenter-sub ink" x="601" y="118" text-anchor="middle" textLength="188" lengthAdjust="spacingAndGlyphs">ENTERTAINMENT</text>

  <!-- presents rule -->
  <g class="rule">
    <polygon class="paper" points="103,173 515,173 515,185 103,185 118,179"/>
    <polygon class="paper" points="685,173 1094,173 1079,179 1094,185 685,185"/>
    <text class="condensed rule-label ink" x="600" y="194" text-anchor="middle" textLength="117" lengthAdjust="spacingAndGlyphs">PRESENTS</text>
  </g>

  <!-- title -->
  <text class="slab title-main ink" x="600" y="348" text-anchor="middle" textLength="991" lengthAdjust="spacingAndGlyphs">HARBOR</text>
  <text class="slab title-sub" x="600" y="462" text-anchor="middle" textLength="991" lengthAdjust="spacingAndGlyphs"><tspan class="ink">LAUGHS LIVE </tspan><tspan class="paper">GETS REAL</tspan></text>
  <text class="slab title-main paper" x="600" y="621" text-anchor="middle" textLength="991" lengthAdjust="spacingAndGlyphs">HONEST</text>

  <!-- hosted by rule -->
  <g class="rule">
    <polygon class="paper" points="103,676 515,676 515,688 103,688 118,682"/>
    <polygon class="paper" points="685,676 1094,676 1079,682 1094,688 685,688"/>
    <text class="condensed rule-label ink" x="602" y="697" text-anchor="middle" textLength="129" lengthAdjust="spacingAndGlyphs">HOSTED BY</text>
  </g>

  <!-- hosts -->
  <ellipse cx="338" cy="1076" rx="255" ry="265" fill="url(#photoTone)" role="img" aria-label="Halftone portrait of host Zolo Brightwave"/>
  <ellipse cx="862" cy="1070" rx="256" ry="270" fill="url(#photoTone)" role="img" aria-label="Halftone portrait of host Marla Vintrow"/>

  <polygon class="ink" points="148,1353 512,1353 498,1378 512,1404 148,1404 162,1378"/>
  <polygon class="ink" points="686,1353 1051,1353 1037,1378 1051,1404 686,1404 700,1378"/>
  <text class="slab host-name sky" x="330" y="1389" text-anchor="middle" textLength="292" lengthAdjust="spacingAndGlyphs">ZOLO BRIGHTWAVE</text>
  <text class="slab host-name sky" x="868" y="1389" text-anchor="middle" textLength="284" lengthAdjust="spacingAndGlyphs">MARLA VINTROW</text>
  <text class="slab ampersand paper" x="600" y="1432" text-anchor="middle">&amp;</text>

  <!-- featuring rule -->
  <g class="rule">
    <polygon class="paper" points="103,1498 515,1498 515,1510 103,1510 118,1504"/>
    <polygon class="paper" points="685,1498 1094,1498 1079,1504 1094,1510 685,1510"/>
    <text class="condensed rule-label ink" x="600" y="1519" text-anchor="middle" textLength="132" lengthAdjust="spacingAndGlyphs">FEATURING</text>
  </g>

  <!-- lineup -->
  <text class="condensed lineup paper" x="599" y="1626" text-anchor="middle" textLength="991" lengthAdjust="spacingAndGlyphs">DEV HALLORAN <tspan class="ink">-</tspan> PRITCHARD SELWYN <tspan class="ink">-</tspan> OWEN TALBRIDGE</text>
  <text class="condensed lineup paper" x="600" y="1689" text-anchor="middle" textLength="907" lengthAdjust="spacingAndGlyphs">NINA OSTRAVA <tspan class="ink">-</tspan> BRIMLEY <tspan class="ink">-</tspan> TOBIN MERRICK <tspan class="ink">-</tspan> &amp; MORE</text>

  <!-- one night rule -->
  <g class="rule">
    <polygon class="paper" points="103,1747 432,1747 432,1759 103,1759 118,1753"/>
    <polygon class="paper" points="773,1747 1094,1747 1079,1753 1094,1759 773,1759"/>
    <text class="slab one-night ink" x="601" y="1770" text-anchor="middle" textLength="303" lengthAdjust="spacingAndGlyphs">ONE NIGHT</text>
  </g>

  <!-- date and venue -->
  <text class="condensed show-date ink" x="600" y="1924" text-anchor="middle" textLength="964" lengthAdjust="spacingAndGlyphs">SATURDAY, AUGUST 22, 2015</text>
  <text class="condensed venue paper" x="600" y="2003" text-anchor="middle" textLength="678" lengthAdjust="spacingAndGlyphs">THE LANTERN ROOM 214 CALDER AVENUE, HARBORVIEW, NY 11290</text>

  <!-- footer -->
  <circle class="ink" cx="397" cy="2113" r="58"/>
  <text class="condensed badge-text paper" x="397" text-anchor="middle"><tspan x="397" y="2100">HARBOR</tspan><tspan x="397" y="2120">LAUGHS</tspan><tspan x="397" y="2140">LIVE</tspan></text>
  <text class="condensed site ink" x="598" y="2136" text-anchor="middle" textLength="221" lengthAdjust="spacingAndGlyphs">PLGRVN.COM</text>
  <circle class="ink" cx="797" cy="2113" r="58"/>
  <text class="condensed badge-text paper" x="797" text-anchor="middle"><tspan x="797" y="2100">GETS</tspan><tspan x="797" y="2120">REAL</tspan><tspan x="797" y="2140">HONEST</tspan></text>
</svg>
</body>
</html>
```